Distinctive Men collection for beard oil, beard balm and hand cream

I have a project: a collection for MEN.
The name of my company is KELV.
- You can play with the writing of the name without any problem.
- I need a label template for my BEARD oil bottles (it needs to have a place where I can change the skin type: dry skin / normal skin / or oily skin)
- I need a round label template for the 50 ml beard balm for the top of the aluminium can. I would like to use something similar for the hand cream so it would fit.

Example of Ingredients:
Beard oil | Oily skin: Ingrédients : Simmondsia chinensis (Jojoba) Seed Oil *, Corylus avellana (Hazelnut) Oil*, Vitis vinifera Seed Oil*, Trocopherol, parfum.

It is a collection, it needs to fit together!

Thank you :-D

Target Market(s)

MEN with a beard

Colors

Designer to choose colors to be used in the design.

Requirements
Must have
• - Labels for the bottles: 1 3/4' X 4'
• - Round label for the beard balm and the hand cream for men: round 1 3/4'
• - For the bottles: the ingredients goes on one end on the label and the Expiration on the other end, so they are "behind" the bottle. Hope I'm clear, I'm not a desgner ;-)
Nice to have
• I have been looking at labels type, and I like the effect of transparent label on amber buttle, BUT it is not at all a must. Just an observation. I am really open to everything!
Should not have
• Important fact: I don't want black and white like almost every bottles on Brindle and in barbershop. I want them both to appeal to trendy barbers AND I want them on Brindle.

```html
<!DOCTYPE html>
<html lang="en">
<head>
<meta charset="utf-8">
<title>KELV Men Collection – Round Tin Labels</title>
<link rel="stylesheet" href="https://fonts.googleapis.com/css2?family=Libre+Baskerville:wght@400;700&display=swap">
<style>
  :root {
    --page-bg: #ececee;
    --navy: #14285a;
    --navy-deep: #0c1a3f;
    --navy-soft: #1d3572;
    --silver: #d9dbe0;
    --silver-light: #f4f5f7;
    --silver-dark: #9a9ea8;
  }
  * { margin: 0; padding: 0; box-sizing: border-box; }
  html, body {
    width: 1200px;
    height: 849px;
    overflow: hidden;
    background: var(--page-bg);
  }
  .collection {
    position: relative;
    width: 1200px;
    height: 849px;
  }
  .tin-label { position: absolute; display: block; }
  .beard-balm-small { left: 76px; top: 64px; width: 312px; height: 312px; }
  .hand-cream { left: 160px; top: 448px; width: 312px; height: 312px; }
  .beard-balm-large { left: 524px; top: 92px; width: 432px; height: 432px; }

  .label-ring-edge { fill: var(--silver-dark); }
  .label-face { fill: var(--navy); }
  .label-vignette { fill: url(#faceShade); }
  .illustration-area { fill: var(--navy-soft); opacity: 0.55; }
  .frame-line {
    fill: none;
    stroke: var(--silver);
    stroke-width: 4;
  }
  .arc-word {
    font-family: "Libre Baskerville", serif;
    font-weight: 700;
    font-size: 22px;
    letter-spacing: 22px;
    fill: var(--silver-light);
  }
  .brand-name {
    font-family: "Libre Baskerville", serif;
    font-weight: 400;
    font-size: 70px;
    fill: var(--silver-light);
  }
  .volume {
    font-family: "Libre Baskerville", serif;
    font-weight: 700;
    font-size: 13px;
    fill: var(--silver-light);
  }
</style>
</head>
<body>
<main class="collection">

  <svg class="tin-label beard-balm-small" viewBox="0 0 400 400" aria-label="KELV beard balm round label">
    <defs>
      <linearGradient id="ringMetal" x1="0" y1="0" x2="1" y2="1">
        <stop offset="0" stop-color="#ffffff"/>
        <stop offset="0.45" stop-color="#c9ccd3"/>
        <stop offset="0.7" stop-color="#f2f3f5"/>
        <stop offset="1" stop-color="#8e929c"/>
      </linearGradient>
      <radialGradient id="faceShade" cx="0.5" cy="0.45" r="0.55">
        <stop offset="0.6" stop-color="#14285a" stop-opacity="0"/>
        <stop offset="1" stop-color="#0c1a3f" stop-opacity="0.85"/>
      </radialGradient>
      <path id="topWordPath" d="M42,200 A158,158 0 0 1 358,200"/>
      <path id="bottomWordPath" d="M22,200 A178,178 0 0 0 378,200"/>
    </defs>
    <circle class="label-ring-edge" cx="200" cy="200" r="199"/>
    <circle cx="200" cy="200" r="196" fill="url(#ringMetal)"/>
    <circle class="label-face" cx="200" cy="200" r="184"/>
    <circle class="label-vignette" cx="200" cy="200" r="184"/>
    <ellipse class="illustration-area" cx="200" cy="215" rx="62" ry="78" role="img" aria-label="Faint beard illustration behind the name"/>
    <circle class="frame-line" cx="200" cy="200" r="150"/>
    <circle class="frame-line" cx="200" cy="200" r="96"/>
    <text class="arc-word"><textPath href="#topWordPath" startOffset="50%" text-anchor="middle">BEARD</textPath></text>
    <text class="arc-word"><textPath href="#bottomWordPath" startOffset="50%" text-anchor="middle">BALM</textPath></text>
    <text class="brand-name" x="200" y="225" text-anchor="middle">Kelv</text>
    <text class="volume" x="78" y="205" text-anchor="middle">50ml</text>
    <text class="volume" x="322" y="205" text-anchor="middle">1.75oz</text>
  </svg>

  <svg class="tin-label hand-cream" viewBox="0 0 400 400" aria-label="KELV hand cream round label">
    <defs>
      <path id="topWordPathHand" d="M42,200 A158,158 0 0 1 358,200"/>
      <path id="bottomWordPathHand" d="M22,200 A178,178 0 0 0 378,200"/>
    </defs>
    <circle class="label-ring-edge" cx="200" cy="200" r="199"/>
    <circle cx="200" cy="200" r="196" fill="url(#ringMetal)"/>
    <circle class="label-face" cx="200" cy="200" r="184"/>
    <circle class="label-vignette" cx="200" cy="200" r="184"/>
    <ellipse class="illustration-area" cx="200" cy="215" rx="58" ry="82" role="img" aria-label="Faint open hand illustration behind the name"/>
    <circle class="frame-line" cx="200" cy="200" r="150"/>
    <circle class="frame-line" cx="200" cy="200" r="96"/>
    <text class="arc-word"><textPath href="#topWordPathHand" startOffset="50%" text-anchor="middle">HAND</textPath></text>
    <text class="arc-word"><textPath href="#bottomWordPathHand" startOffset="50%" text-anchor="middle">CREAM</textPath></text>
    <text class="brand-name" x="200" y="225" text-anchor="middle">Kelv</text>
    <text class="volume" x="78" y="205" text-anchor="middle">50ml</text>
    <text class="volume" x="322" y="205" text-anchor="middle">1.75oz</text>
  </svg>

  <svg class="tin-label beard-balm-large" viewBox="0 0 400 400" aria-label="KELV beard balm round label, large view">
    <defs>
      <path id="topWordPathLarge" d="M42,200 A158,158 0 0 1 358,200"/>
      <path id="bottomWordPathLarge" d="M22,200 A178,178 0 0 0 378,200"/>
    </defs>
    <circle class="label-ring-edge" cx="200" cy="200" r="199"/>
    <circle cx="200" cy="200" r="196" fill="url(#ringMetal)"/>
    <circle class="label-face" cx="200" cy="200" r="184"/>
    <circle class="label-vignette" cx="200" cy="200" r="184"/>
    <ellipse class="illustration-area" cx="200" cy="215" rx="62" ry="78" role="img" aria-label="Faint beard illustration behind the name"/>
    <circle class="frame-line" cx="200" cy="200" r="150"/>
    <circle class="frame-line" cx="200" cy="200" r="96"/>
    <text class="arc-word"><textPath href="#topWordPathLarge" startOffset="50%" text-anchor="middle">BEARD</textPath></text>
    <text class="arc-word"><textPath href="#bottomWordPathLarge" startOffset="50%" text-anchor="middle">BALM</textPath></text>
    <text class="brand-name" x="200" y="225" text-anchor="middle">Kelv</text>
    <text class="volume" x="78" y="205" text-anchor="middle">50ml</text>
    <text class="volume" x="322" y="205" text-anchor="middle">1.75oz</text>
  </svg>

</main>
</body>
</html>
```